Hair and Wellness Brochure and Pricelist design

I am requiring a brochure that has a fresh, though alternative design. My business name is The Quiet Harbor Hair and Wellness. I have a very professional approach to my work and love to give that little bit extra to all of my clients. My passion for health, has led me to channel my business alternatively by using non toxic colours and styling products and through that same vein, I have studied Aromatherapy, Indian Head Massage and Reiki...all additional services I use where required.
My studio has very neutral tones of beige,white and beech wood but these tones aren't necessarily required for the brochure.I like to create a space of calm, peace and quiet, where my clients feel refreshed and rejuvenated..

```html
<!DOCTYPE html>
<html lang="en">
<head>
<meta charset="utf-8">
<title>Hair and Wellness Brochure</title>
<link rel="stylesheet" href="https://fonts.googleapis.com/css2?family=Caveat:wght@500&family=Tinos&display=swap">
<style>
  :root {
    --paper: #f6e8d9;
    --panel: #ecdccb;
    --taupe: #8d7e6d;
    --heading: #766a60;
    --body: #8a7b6d;
    --light: #f8f1e8;
    --skin: #e8d3c4;
  }
  * { margin: 0; padding: 0; box-sizing: border-box; }
  html, body { width: 1200px; height: 900px; overflow: hidden; background: var(--paper); }
  .brochure { position: relative; width: 1200px; height: 900px; background: var(--paper); }
  .brochure > * { position: absolute; }

  .script-heading {
    font-family: "Caveat", cursive;
    font-weight: 500;
    color: var(--heading);
    line-height: 1;
    white-space: nowrap;
    z-index: 2;
  }
  .script-heading--title { left: 44px; top: 36px; font-size: 70px; letter-spacing: 2px; }
  .script-heading--section { font-size: 40px; }

  .copy {
    font-family: "Tinos", "Times New Roman", serif;
    font-size: 23px;
    letter-spacing: 1.1px;
    line-height: 29px;
    color: var(--body);
    white-space: nowrap;
    z-index: 1;
  }
  .text-panel { background: var(--panel); }

  .photo-slot { display: block; }
  .info-box {
    background: var(--taupe);
    color: var(--light);
    font-family: "Tinos", "Times New Roman", serif;
    font-size: 23px;
    letter-spacing: 1.1px;
    line-height: 29px;
  }
  .divider { background: var(--taupe); }
</style>
</head>
<body>
<main class="brochure">

  <h1 class="script-heading script-heading--title">Lorem Ipsum</h1>
  <p class="copy" style="left:33px; top:117px;">
    Lorem ipsum dolor sit amet, cons<br>ectetur adipiscing elit. Maecenas<br>at ullamcorper massa. Ut tellus r<br>isus, iaculis in velit non, aliquet<br>varius est. Nullam adipiscing con.
  </p>

  <div class="text-panel" style="left:32px; top:318px; width:349px; height:187px;"></div>
  <h2 class="script-heading script-heading--section" style="left:158px; top:282px; letter-spacing:2px;">Aromatherapy</h2>
  <p class="copy" style="left:37px; top:321px;">
    Lorem ipsum dolor sit amet, con<br>sectetur adipiscing elit. Maecena<br>s at ullamcorper massa. Ut tellus<br>risus, iaculis in velit non, aliquet<br>varius est. Nullam adipiscing con<br>sequat tortor, quis lacinia ipsum
  </p>

  <svg class="photo-slot" role="img" aria-label="Aromatherapy still life with a lavender candle, wooden bowl and dried lavender" style="left:35px; top:530px;" width="344" height="180">
    <defs>
      <linearGradient id="aroma-tones" x1="0" y1="0" x2="1" y2="1">
        <stop offset="0" stop-color="#9a7fb0"/>
        <stop offset="0.5" stop-color="#8a6a55"/>
        <stop offset="1" stop-color="#4a3528"/>
      </linearGradient>
    </defs>
    <rect width="344" height="180" fill="url(#aroma-tones)"/>
  </svg>

  <div class="info-box" style="left:37px; top:733px; width:338px; height:135px; padding:14px 0 0 38px;">
    contacts for appuntament<br>days and times for these<br>therapies
  </div>

  <h2 class="script-heading script-heading--section" style="left:463px; top:56px; font-size:46px; letter-spacing:2.5px;">Massage Room</h2>
  <div class="info-box" style="left:430px; top:135px; width:343px; height:227px; display:flex; align-items:center; justify-content:center; padding-bottom:22px;">
    photo massage room
  </div>

  <div class="text-panel" style="left:433px; top:423px; width:344px; height:277px;"></div>
  <h2 class="script-heading script-heading--section" style="left:449px; top:392px; letter-spacing:2.5px;">Indian head massage</h2>
  <p class="copy" style="left:441px; top:439px;">
    Lorem ipsum dolor sit amet, con<br>sectetur adipiscing elit. Maecena<br>s at ullamcorper massa. Ut tellus<br>risus, iaculis in velit non, aliquet<br>varius est. Nullam adipiscing con<br>sequat tortor, quis lacinia ipsum<br>varius est. Nullam adipiscing con<br>sequat tortor, quis lacinia ipsum
  </p>

  <svg class="photo-slot" role="img" aria-label="Client receiving an Indian head massage" style="left:433px; top:722px;" width="341" height="143">
    <defs>
      <linearGradient id="head-tones" x1="0" y1="0" x2="1" y2="0">
        <stop offset="0" stop-color="#d9c2b2"/>
        <stop offset="0.6" stop-color="#e8d3c4"/>
        <stop offset="1" stop-color="#faf6f2"/>
      </linearGradient>
    </defs>
    <rect width="341" height="143" fill="url(#head-tones)"/>
  </svg>

  <div class="text-panel" style="left:825px; top:62px; width:342px; height:220px;"></div>
  <h2 class="script-heading script-heading--section" style="left:951px; top:28px; letter-spacing:1.5px;">Reiki massage</h2>
  <p class="copy" style="left:831px; top:63px;">
    varius est. Nullam adipiscing con<br>sequat tortor, quis lacinia ipsum<br>varius est. Nullam adipiscing con<br>sequat tortor, quis lacinia ipsum<br>varius est. Nullam adipiscing con<br>sequat tortor, quis lacinia ipsum<br>varius est. Nullam adipiscing con
  </p>

  <svg class="photo-slot" role="img" aria-label="Client relaxing during a Reiki session" style="left:828px; top:305px;" width="339" height="157">
    <defs>
      <linearGradient id="reiki-tones" x1="0" y1="0" x2="1" y2="0">
        <stop offset="0" stop-color="#e4cbb8"/>
        <stop offset="0.55" stop-color="#f0e2d6"/>
        <stop offset="1" stop-color="#fbf8f5"/>
      </linearGradient>
    </defs>
    <rect width="339" height="157" fill="url(#reiki-tones)"/>
  </svg>

  <div class="divider" style="left:830px; top:487px; width:341px; height:7px;"></div>

  <p class="copy" style="left:824px; top:512px;">
    Lorem ipsum dolor sit amet, conse<br>ctetur adipiscing elit. Maecenas at<br>ullamcorper massa. Ut tellus risus,<br>iaculis in velit non, aliquet varius<br>est. Nullam adipiscing consequat<br>tortor, quis lacinia ipsum condime<br>ntum et. Nulla auctor aliquet conse<br>quat. Fusce dictum dignissim nisl,<br>mollis eleifend lorem iaculis et.<br>ntum et. Nulla auctor aliquet conse<br>quat. Fusce dictum dignissim nisl,<br>mollis eleifend lorem iaculis et.
  </p>

</main>
</body>
</html>
```